Webdesign für IT-Dienstleister
Zielgruppe
Seit 1997 bieten wir erstklassige IT-Dienstleistungen Mainz an, die darauf ausgerichtet sind, Unternehmen und Privatkunden mit kompetenter Beratung, zuverlässiger Unterstützung und modernen Technologielösungen zur Seite zu stehen.
Umfassende Computer-Serviceleistungen
Unser Computer-Service Mainz beinhaltet eine Reihe von Dienstleistungen, die darauf abzielen, die Leistungsfähigkeit Ihrer IT-Infrastruktur zu optimieren und zu erhalten. Von der Fehlerdiagnose bis hin zur Wartung bieten wir ein Rundum-Sorglos-Paket für Ihre Hardware und Software.
Professionelle Fehleranalyse und Reparatur
Optimierung von Betriebssystemen und Anwendungen
Regelmäßige Wartungsarbeiten zur Vorbeugung von Ausfällen
Ersetzen und Aufrüsten von Hardware-Komponenten
Aufgabenstellung
Ich hätte gern ein modernes Design. Ein Logo vorhanden, sollte mit eingebaut werden.
Ansonsten hätte ich gerne eine einzelne Webseite mit den Firmen Infos (und den Links zu Sozial Media) und einer extra Impressum Seite. Und wenn möglich noch ein Anfrage Formular.
Am liebsten wäre ein Format welches ich in WordPress verarbeiten werden kann.
(Logo wird noch nachgereicht)

```html
<!DOCTYPE html>
<html lang="de">
<head>
<meta charset="utf-8">
<title>Impressum – IT-Dienstleistungen Kilmar</title>
<link href="https://fonts.googleapis.com/css2?family=Poppins:wght@400;500;600&display=swap" rel="stylesheet">
<style>
:root{
  --navy:#13213f;
  --blue:#1a9ad6;
  --white:#ffffff;
  --line:#13213f;
  --muted:#8a93a6;
  --divider:#e3e6ec;
  --foot-divider:#2d3b5a;
}
*{margin:0;padding:0;box-sizing:border-box}
html,body{width:1200px;height:1019px;overflow:hidden}
body{font-family:'Poppins',sans-serif;color:var(--navy);background:var(--white);position:relative}
.topbar{position:absolute;left:669px;top:0;width:358px;height:25px;background:var(--blue);border-radius:0 0 3px 3px;display:flex;align-items:center;justify-content:space-around;color:var(--white);font-size:8.6px;padding:0 8px}
.topbar span{display:flex;align-items:center;gap:4px}
.topbar svg{width:11px;height:11px}
.header{position:absolute;left:0;top:0;width:1200px;height:81px;border-bottom:1px solid var(--divider)}
.brand{position:absolute;display:flex;align-items:center;gap:10px}
.header .brand{left:173px;top:17px}
.brand-dot{width:46px;height:46px;border-radius:50%;border:2.5px solid var(--navy)}
.brand-name{font-size:15px;font-weight:500;color:var(--navy);white-space:nowrap}
.nav{position:absolute;left:502px;top:45px;display:flex;gap:32px;font-size:10.5px;font-weight:500}
.cta{position:absolute;left:892px;top:40px;display:flex}
.pill{height:26px;border:1px solid var(--navy);border-radius:13px;padding:0 14px;display:flex;align-items:center;font-size:10.5px;font-weight:500;background:var(--white);white-space:nowrap}
.circle-btn{width:26px;height:26px;border:1px solid var(--navy);border-radius:50%;display:flex;align-items:center;justify-content:center;background:var(--white)}
.circle-btn svg{width:11px;height:11px}
h1{position:absolute;left:0;top:128px;width:1200px;text-align:center;font-size:31px;font-weight:500}
.row{position:absolute;left:173px;width:854px;border-top:1px solid var(--line);font-size:10px;line-height:17.5px}
.row .label{position:absolute;left:208px;top:20px;font-weight:500}
.row .value{position:absolute;left:427px;top:20px}
.row a{color:var(--blue);text-decoration:none}
.end-line{position:absolute;left:173px;top:589px;width:854px;border-top:1px solid var(--line)}
.newsletter h2{position:absolute;top:673px;width:1200px;text-align:center;font-size:15px;font-weight:500}
.newsletter p{position:absolute;top:702px;width:1200px;text-align:center;font-size:11.3px;line-height:17.5px;font-weight:500}
.footer{position:absolute;left:0;top:788px;width:1200px;height:231px;background:var(--navy)}
.signup{position:absolute;left:381px;top:765px;width:438px;height:46px;background:var(--white);border-radius:23px;box-shadow:0 4px 14px rgba(19,33,63,.15);display:flex;align-items:center;padding:0 9px 0 21px;z-index:2}
.signup .field{flex:1;color:var(--blue);font-size:10px}
.signup .pill{font-size:10px}
.footer-brand{left:173px;top:886px}
.footer-brand .brand-dot{border-color:var(--white)}
.footer-brand .brand-name{color:var(--white)}
.social{position:absolute;right:173px;top:907px;display:flex;align-items:center;gap:6px;color:var(--white);font-size:10.3px;font-weight:500}
.social .label{margin-right:8px}
.social i{width:27px;height:27px;border-radius:50%;background:var(--white);display:block}
.foot-line{position:absolute;left:173px;top:955px;width:854px;border-top:1px solid var(--foot-divider)}
.copy{position:absolute;left:173px;top:970px;color:var(--muted);font-size:10px}
.legal{position:absolute;right:173px;top:970px;display:flex;gap:22px;color:var(--white);font-size:10px;font-weight:500}
</style>
</head>
<body>
<header class="header">
  <div class="brand">
    <div class="brand-dot"></div>
    <span class="brand-name">IT-Dienstleistungen Kilmar</span>
  </div>
  <nav class="nav"><span>Service &amp; Wartung</span><span>DSL &amp; Internet</span><span>PC &amp; Server</span><span>Kontakt</span></nav>
  <div class="cta"><span class="pill">Anfrage senden</span><span class="circle-btn"><svg viewBox="0 0 12 12"><path d="M2 10L10 2M4 2h6v6" fill="none" stroke="#13213f" stroke-width="1.2"/></svg></span></div>
</header>
<div class="topbar">
  <span><svg viewBox="0 0 12 12"><circle cx="6" cy="6" r="5.3" fill="none" stroke="#fff"/><path d="M4 3.5l1 1.5-.6.7a4 4 0 0 0 2 2l.7-.6 1.4 1-.7 1C5.5 9 3 6.5 3 4.2z" fill="#fff"/></svg>+49 (0) 6131. 48 21 570</span>
  <span><svg viewBox="0 0 12 12"><rect x="1" y="2.5" width="10" height="7" fill="none" stroke="#fff"/><path d="M1 2.5l5 4 5-4" fill="none" stroke="#fff"/></svg>anfrage@kilmar-it.de</span>
  <span><svg viewBox="0 0 12 12"><rect x="1.5" y="1.5" width="9" height="9" fill="none" stroke="#fff"/><path d="M3 4h6M3 6h6M3 8h4" stroke="#fff"/></svg>Newsletter</span>
</div>

<h1>Impressum</h1>

<section class="row" style="top:191px;height:216px">
  <div class="label">Firmensitz</div>
  <div class="value">IT Dienstleistungen Kilmar<br>Lindenhofweg 8<br>55122 Mainz, Deutschland<br><br>Telefon: +49 [0] 6131. 48 21 570<br>Telefax: +49 [0] 6131. 48 21 571<br>E-Mail: j.brehm@kilmar-it.de<br><br>Umsatzsteuer-ID: DE204518779<br>Vertreten durch: Jonas Brehm</div>
</section>
<section class="row" style="top:407px;height:182px">
  <div class="label">Online-Streitbeteiligung</div>
  <div class="value">Plattform der EU-Kommission<br>zur Online-Streitbeilegung:<br><a href="#">https://streitschlichtung-portal.example/odr</a><br><br>Wir sind zur Teilnahme an einem<br>Streitbeilegungsverfahren vor einer<br>Verbraucherschlichtungsstelle weder<br>verpflichtet noch bereit.</div>
</section>
<div class="end-line"></div>

<section class="newsletter">
  <h2>Newsletter abonnieren</h2>
  <p>Verpassen Sie keine aktuellen Angebote und Neuigkeiten aus unserem Hause<br>und abonnieren unseren unverbindlichen Newsletter.</p>
</section>
<form class="signup">
  <span class="field">Ihre E-Mail-Adresse*</span>
  <span class="pill">Newsletter abonnieren</span><span class="circle-btn"><svg viewBox="0 0 12 12"><path d="M2 10L10 2M4 2h6v6" fill="none" stroke="#13213f" stroke-width="1.2"/></svg></span>
</form>

<footer class="footer"></footer>
<div class="brand footer-brand">
  <div class="brand-dot"></div>
  <span class="brand-name">IT-Dienstleistungen Kilmar</span>
</div>
<div class="social"><span class="label">Folgen Sie uns bei Social Media</span><i></i><i></i><i></i><i></i></div>
<div class="foot-line"></div>
<div class="copy">© 2025 IT-Dienstleistungen Kilmar. All rights reserved.</div>
<div class="legal"><span>Impressum</span><span>Datenschutzerklärung</span><span>Kontakt</span></div>
</body>
</html>
```